Graphic Design Template for Digital Marketing Strategy

I require a template designing for a digital marketing strategy template, this will be a downloadable 2 page pdf.

One side will have a diagram showcasing all relevant DM strategies and how businesses should implement them, the following page will have a table that helps in the planning process.

I will provide all the content, however I need it to look professional, more importantly I need it to be a usable document for a business that lacks DM knowledge, so it needs to have implementable steps!

I have attached a similar document, this is good, however it does not get across the steps needs to be taken.

Also attached our logo.

Any questions please ask.

Owen

```html
<!DOCTYPE html>
<html lang="en">
<head>
<meta charset="utf-8">
<title>Web Strategy Template</title>
<link rel="stylesheet" href="https://fonts.googleapis.com/css2?family=Didact+Gothic&family=Arimo:wght@400;700&display=swap">
<style>
:root{
  --page-bg:#ffffff;
  --sheet-blue:#2b6fbc;
  --sheet-blue-deep:#1f5aa3;
  --sheet-glow:#4a8fd6;
  --tab-navy:#1b4a8c;
  --ink-white:#ffffff;
  --panel-tint:rgba(255,255,255,0.10);
  --heading-blue:#1f63b4;
  --website-blue:#1b86d8;
  --website-light:#5fb6f0;
  --magenta:#b4187c;
  --magenta-light:#d23a98;
  --table-grey:#d4d6d9;
  --table-line:#b9bcc0;
  --table-ink:#3a3d42;
  --label-blue:#2d72c0;
  --brand-navy:#16335e;
  --brand-dot:#2f93e0;
}
*{box-sizing:border-box;margin:0;padding:0}
html,body{width:1200px;height:900px;overflow:hidden;background:var(--page-bg)}
body{position:relative;font-family:"Didact Gothic",sans-serif;color:var(--ink-white)}

.sheet{position:absolute;width:566px;height:414px;overflow:hidden;
  background:radial-gradient(circle at 50% 48%,var(--sheet-glow) 0,rgba(74,143,214,0) 45%),
             linear-gradient(135deg,var(--sheet-blue) 0%,var(--sheet-blue-deep) 100%);
  box-shadow:0 0 3px rgba(0,0,0,0.25)}
.at-top{top:26px}.at-bottom{top:460px}
.at-left{left:24px}.at-right{left:610px}

.sheet-tab{position:absolute;left:0;top:0;height:29px;width:160px;padding-left:40px;
  background:var(--tab-navy);clip-path:polygon(0 0,100% 0,88% 100%,0 100%);
  font-size:14px;line-height:29px;color:var(--ink-white)}
.sheet-tab.wide{width:175px;font-size:12px}
.tab-mark{position:absolute;left:16px;top:6px;width:17px;height:17px;border:2px solid var(--ink-white);border-radius:50%}

.search-box{position:absolute;left:203px;top:10px;width:157px;height:42px;background:#fff;border-radius:2px}
.search-brand{text-align:center;color:var(--heading-blue);font-size:15px;line-height:20px;margin-top:2px}
.search-row{display:flex;align-items:center;padding:0 5px;gap:4px;font-size:8px;color:#333}
.search-row i{flex:1;height:9px;background:#dfeaf6;border:1px solid #c5d6ea}

.list-panel{position:absolute;top:56px;background:var(--panel-tint);border-radius:2px}
.list-panel h2{background:#fff;color:var(--heading-blue);font-weight:400;font-size:12.5px;text-align:center;line-height:18px;border-radius:2px 2px 0 0}
.backlinks{left:15px;width:137px;height:272px}
.outcomes{left:413px;width:136px;height:271px}
.list-panel ul{list-style:none;font-size:7.3px}
.backlinks ul{padding:7px 0 0 13px}
.backlinks li{height:14px;line-height:14px}
.outcomes ul{padding:3px 0 0 8px}
.outcomes li{height:12.3px;line-height:12.3px}
.outcomes li.group{margin-top:3px}
.outcomes li.step{padding-left:9px}
.box{display:inline-block;width:7px;height:7px;background:#fff;margin-right:5px;vertical-align:-1px}

.diagram{position:absolute;left:0;top:0;width:566px;height:414px}
.diagram text{font-family:"Didact Gothic",sans-serif;fill:var(--ink-white)}

.footnote{position:absolute;left:14px;top:356px;width:186px;font-size:4.6px;line-height:5.6px;color:var(--ink-white)}
.footnote.wide{left:34px;width:496px}
.footnote.wide+.footnote.wide{top:383px}
.corner{position:absolute;right:0;bottom:0;width:118px;height:86px;background:#fff;clip-path:polygon(100% 0,100% 100%,0 100%)}
.brand{position:absolute;right:10px;bottom:8px;display:flex;align-items:center;gap:4px;
  font-size:7.5px;line-height:8px;color:var(--brand-navy);text-align:right;letter-spacing:0.3px}
.brand-dot{width:18px;height:18px;border-radius:50%;background:var(--brand-dot)}

/* planning sheet */
.client-fields{position:absolute;left:270px;top:15px;width:262px;font-size:7px;color:var(--ink-white)}
.client-fields div{display:flex;align-items:flex-end;height:10px}
.client-fields span{width:90px;text-align:right;padding-right:3px}
.client-fields i{flex:1;border-bottom:1px solid var(--ink-white);height:7px}

.plan-table{position:absolute;left:34px;top:42px;width:495px;height:304px;background:#fff;
  font-family:Arimo,sans-serif;color:var(--table-ink);font-size:6.2px;line-height:7.4px}
.plan-row{display:grid;grid-template-columns:34px 125px 168px 168px;border-bottom:1px solid var(--table-line)}
.plan-row.shaded{background:var(--table-grey)}
.plan-row>div{border-right:1px solid var(--table-line);padding:1px 3px}
.plan-row>div:last-child{border-right:0}
.row-label{color:var(--label-blue);display:flex;align-items:center;justify-content:center;font-family:"Didact Gothic",sans-serif;font-size:6.4px}
.row-who{height:31px}.row-what{height:67px}.row-why{height:35px}.row-where{height:28px}.row-how{height:101px}
.q-main{font-size:6.6px}
.q-note{font-size:5.4px}
.q-split{border-bottom:1px solid var(--table-line);margin:0 -3px 1px;padding:0 3px 1px}
.q-gap{height:14px}
.row-when{position:absolute;left:0;top:264px;width:495px;height:40px;border-top:1px solid var(--table-line);
  display:grid;grid-template-columns:34px 283px 12px 83px 40px 43px}
.row-when>div{border-right:1px solid var(--table-line)}
.row-when>div:last-child{border-right:0}
.when-lines div,.score-lines div{height:10px;line-height:9px;border-bottom:1px solid var(--table-line)}
.when-lines div{display:grid;grid-template-columns:82px 1fr}
.when-lines span{text-align:right;padding-right:2px;font-size:6.4px}
.score-lines div{padding-left:3px;font-size:5.6px}
.score-tag{color:var(--label-blue);font-size:4.6px;writing-mode:vertical-rl;transform:rotate(180deg);text-align:center;letter-spacing:0.5px}
.score-head{color:#c7c9cc;font-size:7px;display:flex;align-items:center;justify-content:center}
.blank-col div{height:10px;border-bottom:1px solid var(--table-line)}
</style>
</head>
<body>

<!-- Strategy diagram sheet -->
<section class="sheet at-top at-left">
  <header class="sheet-tab"><span class="tab-mark"></span>Web Strategy</header>
  <div class="search-box"><div class="search-brand">Seekly</div><div class="search-row"><span>Search</span><i></i></div></div>
  <div class="list-panel backlinks"><h2>BACK LINKS</h2><ul>
    <li><span class="box"></span>Blogs →</li><li><span class="box"></span>News Websites →</li><li><span class="box"></span>Guest Blog Posts →</li><li><span class="box"></span>Testimonials →</li><li><span class="box"></span>Speaker Bios →</li><li><span class="box"></span>Expert Articles →</li><li><span class="box"></span>Industry Partners →</li><li><span class="box"></span>Blog Directories →</li><li><span class="box"></span>News Releases →</li><li><span class="box"></span>Affiliates →</li><li><span class="box"></span>Awards →</li><li><span class="box"></span>Galleries →</li><li><span class="box"></span>Infographics →</li><li><span class="box"></span>Events →</li><li><span class="box"></span>Threadly →</li><li><span class="box"></span>Wanderly →</li><li><span class="box"></span>Upvoter →</li>
  </ul></div>
  <div class="list-panel outcomes"><h2>OUTCOMES</h2><ul>
    <li class="group"><span class="box"></span>PURCHASE</li><li class="step">→ Buy</li><li class="step">→ Donate</li><li class="step">→ Renew</li>
    <li class="group"><span class="box"></span>ENQUIRE</li><li class="step">→ Contact Us Form</li><li class="step">→ Questionnaires</li><li class="step">→ Apply Now</li>
    <li class="group"><span class="box"></span>CONNECT</li><li class="step">→ Follow on Chirper</li><li class="step">→ Subscribe to Emails</li><li class="step">→ ‘Like’ on Mingle</li><li class="step">→ Subscribe to Blog</li><li class="step">→ Connect on ProLink</li>
    <li class="group"><span class="box"></span>DOWNLOAD</li><li class="step">→ Flagship Content</li><li class="step">→ Premium Content</li><li class="step">→ E-books</li><li class="step">→ Templates</li>
  </ul></div>
  <svg class="diagram" viewBox="0 0 566 414" aria-hidden="true">
    <circle cx="207" cy="74" r="8" fill="#fff"/><circle cx="205.5" cy="72.5" r="3" fill="none" stroke="#1f63b4" stroke-width="1.2"/><line x1="207.5" y1="74.5" x2="210.5" y2="77.5" stroke="#1f63b4" stroke-width="1.4"/>
    <text x="218" y="76" font-size="11">SEO</text><text x="214" y="84" font-size="5">Organic Searches</text>
    <circle cx="298" cy="74" r="8" fill="#fff"/><circle cx="298" cy="74" r="4.5" fill="#2f93e0"/>
    <text x="309" y="76" font-size="11">SEM</text><text x="309" y="84" font-size="5">Seekly Ads</text>
    <g stroke="#fff" stroke-width="1" fill="none"><path d="M245 89V103M242 100l3 3 3-3"/><path d="M326 89V103M323 100l3 3 3-3"/><path d="M342 209H384M380 206l4 3-4 3"/></g>
    <circle cx="282" cy="164" r="52" fill="none" stroke="#fff" stroke-width="2.2"/>
    <circle cx="282" cy="303" r="84" fill="none" stroke="#fff" stroke-width="2.2"/>
    <circle cx="282" cy="168" r="33" fill="var(--website-blue)" stroke="var(--website-light)" stroke-width="2"/>
    <text x="282" y="164" font-size="10.5" text-anchor="middle">Website</text>
    <rect x="270" y="170" width="24" height="13" fill="#fff"/><rect x="270" y="170" width="24" height="3" fill="#9cc9ee"/>
    <circle cx="282" cy="305" r="53" fill="var(--magenta)" stroke="var(--magenta-light)" stroke-width="2"/>
    <text x="282" y="298" font-size="11" text-anchor="middle">Social Media</text>
    <text x="282" y="311" font-size="11" text-anchor="middle">Content &amp;</text>
    <text x="282" y="324" font-size="11" text-anchor="middle">Marketing</text>
    <g stroke="#dce8f5" stroke-width="1.5" fill="#fff">
      <circle cx="282" cy="111" r="13"/><circle cx="231" cy="169" r="11"/><circle cx="336" cy="164" r="11"/><circle cx="282" cy="218" r="11"/>
      <circle cx="330" cy="236" r="11"/><circle cx="358" cy="268" r="11"/><circle cx="364" cy="304" r="11"/><circle cx="356" cy="344" r="11"/>
      <circle cx="329" cy="374" r="11"/><circle cx="282" cy="387" r="11"/><circle cx="238" cy="374" r="11"/><circle cx="210" cy="344" r="11"/>
      <circle cx="202" cy="304" r="11"/><circle cx="209" cy="268" r="11"/><circle cx="235" cy="232" r="11"/>
    </g>
    <rect x="274" y="104" width="16" height="11" fill="#2f93e0"/><rect x="279" y="115" width="6" height="3" fill="#777"/>
    <rect x="227" y="162" width="8" height="14" rx="1.5" fill="#2f93e0"/>
    <rect x="331" y="158" width="10" height="12" fill="#f0c36a"/>
    <circle cx="282" cy="218" r="7.5" fill="#f39a1e"/>
    <circle cx="330" cy="236" r="7.5" fill="#2d4f8f"/><circle cx="358" cy="268" r="7.5" fill="#1e7cc2"/>
    <circle cx="364" cy="304" r="7.5" fill="#d4483a"/><circle cx="356" cy="344" r="7.5" fill="#45b3e8"/>
    <circle cx="329" cy="374" r="7.5" fill="#6c3fa0"/><circle cx="282" cy="387" r="7.5" fill="#2f93e0"/>
    <circle cx="238" cy="374" r="7.5" fill="#4a4541"/><circle cx="210" cy="344" r="7.5" fill="#c8232c"/>
    <circle cx="202" cy="304" r="7.5" fill="#2fb07a"/><circle cx="235" cy="232" r="7.5" fill="#d8342e"/>
    <rect x="203" y="264" width="12" height="8" fill="#c9ccd1"/><path d="M203 264l6 4.5 6-4.5" fill="none" stroke="#888" stroke-width="0.8"/>
    <g font-size="5.5">
      <text x="216" y="165" text-anchor="end">Mobile &amp; Tablet</text><text x="216" y="171" text-anchor="end">Friendly Site</text>
      <text x="352" y="166">Landing Pages</text>
      <text x="282" y="237" text-anchor="middle">Blog</text>
      <text x="344" y="235">Mingle</text><text x="372" y="270">ProLink</text><text x="378" y="306">Seekly Plus</text>
      <text x="370" y="346">Chirper</text><text x="343" y="374">Podcasts &amp;</text><text x="343" y="380">Webinars</text>
      <text x="282" y="405" text-anchor="middle">Apps</text>
      <text x="223" y="376" text-anchor="end">Photon</text><text x="196" y="346" text-anchor="end">Pinspace</text>
      <text x="188" y="302" text-anchor="end">Loopy</text>
      <text x="195" y="264" text-anchor="end">Email</text><text x="195" y="270" text-anchor="end">Marketing</text>
      <text x="221" y="234" text-anchor="end">Vidora</text>
    </g>
  </svg>
  <p class="footnote">* Start with the website, then point every search, link and social channel back to it. Tick each back link you can win, choose one outcome per visitor and review the results monthly so you can see which channels bring real enquiries.</p>
  <div class="corner"></div>
  <div class="brand"><span class="brand-dot"></span><span>CLOUDLINE<br>DIGITAL</span></div>
</section>

<!-- Planning table sheet -->
<section class="sheet at-top at-right">
  <header class="sheet-tab wide"><span class="tab-mark"></span>Web Strategy Planning</header>
  <div class="client-fields"><div><span>COMPANY:</span><i></i></div><div><span>PRODUCT/SERVICE:</span><i></i></div></div>
  <div class="plan-table">
    <div class="plan-row shaded row-who"><div class="row-label">WHO</div><div><div class="q-main">Buyer Persona</div><div class="q-main">Description</div><div class="q-note">Who is this person?</div></div><div>1:</div><div>2:</div></div>
    <div class="plan-row row-what"><div class="row-label">WHAT</div><div><div class="q-split"><div class="q-main">Problems you solve for this buyer?</div><div class="q-note">Why are they buying from you?</div></div><div class="q-main">Actions you'd like them to take:</div><div class="q-note">Purchase</div><div class="q-note">Enquire</div><div class="q-note">Connect</div><div class="q-note">Download</div></div><div></div><div></div></div>
    <div class="plan-row shaded row-why"><div class="row-label">WHY</div><div><div class="q-main">How are you remarkable?</div><div class="q-main" style="margin-top:6px">Proof</div><div class="q-note">Guarantees, testimonials, press etc</div></div><div></div><div></div></div>
    <div class="plan-row row-where"><div class="row-label">WHERE</div><div><div class="q-main">Where are they?</div><div class="q-note">Seekly, blogs, Mingle, Chirper etc</div><div class="q-note">Who do they trust?</div></div><div></div><div></div></div>
    <div class="plan-row shaded row-how"><div class="row-label">HOW</div><div><div class="q-main">Content is King (Strategy)</div><div class="q-note">What will you publish?</div><div class="q-gap"></div><div class="q-note">Keywords buyers type into Seekly.</div><div class="q-main" style="margin-top:3px">Marketing is Queen (Tactics)</div><div class="q-note">Blog, Chirper, Vidora, email newsletter, e-books, Mingle podcasts etc</div></div><div></div><div></div></div>
    <div class="row-when">
      <div class="row-label">WHEN</div>
      <div class="when-lines"><div><span>Things to do this week:</span></div><div><span>... this month:</span></div><div><span>... this quarter:</span></div><div><span>... this year:</span></div></div>
      <div class="score-tag">SCORECARD</div>
      <div class="score-lines"><div>No. of Purchases:</div><div>No. of Enquiries:</div><div>No. of Connections:</div><div>No. of Downloads:</div></div>
      <div class="score-head">GOAL</div>
      <div class="score-head">RESULT</div>
    </div>
  </div>
  <p class="footnote wide">* Fill in one column per buyer persona. Describe who they are, what problem you solve, where they spend time online and which actions you want them to take, then set weekly goals.</p>
  <p class="footnote wide">* Use the scorecard to record each goal beside its result at the end of every month, and move effort towards the channels that bring the most purchases, enquiries, connections and downloads.</p>
  <div class="corner"></div>
  <div class="brand"><span class="brand-dot"></span><span>CLOUDLINE<br>DIGITAL</span></div>
</section>

<!-- Strategy diagram sheet, second row -->
<section class="sheet at-bottom at-left">
  <header class="sheet-tab"><span class="tab-mark"></span>Web Strategy</header>
  <div class="search-box"><div class="search-brand">Seekly</div><div class="search-row"><span>Search</span><i></i></div></div>
  <div class="list-panel backlinks"><h2>BACK LINKS</h2><ul>
    <li><span class="box"></span>Blogs →</li><li><span class="box"></span>News Websites →</li><li><span class="box"></span>Guest Blog Posts →</li><li><span class="box"></span>Testimonials →</li><li><span class="box"></span>Speaker Bios →</li><li><span class="box"></span>Expert Articles →</li><li><span class="box"></span>Industry Partners →</li><li><span class="box"></span>Blog Directories →</li><li><span class="box"></span>News Releases →</li><li><span class="box"></span>Affiliates →</li><li><span class="box"></span>Awards →</li><li><span class="box"></span>Galleries →</li><li><span class="box"></span>Infographics →</li><li><span class="box"></span>Events →</li><li><span class="box"></span>Threadly →</li><li><span class="box"></span>Wanderly →</li><li><span class="box"></span>Upvoter →</li>
  </ul></div>
  <div class="list-panel outcomes"><h2>OUTCOMES</h2><ul>
    <li class="group"><span class="box"></span>PURCHASE</li><li class="step">→ Buy</li><li class="step">→ Donate</li><li class="step">→ Renew</li>
    <li class="group"><span class="box"></span>ENQUIRE</li><li class="step">→ Contact Us Form</li><li class="step">→ Questionnaires</li><li class="step">→ Apply Now</li>
    <li class="group"><span class="box"></span>CONNECT</li><li class="step">→ Follow on Chirper</li><li class="step">→ Subscribe to Emails</li><li class="step">→ ‘Like’ on Mingle</li><li class="step">→ Subscribe to Blog</li><li class="step">→ Connect on ProLink</li>
    <li class="group"><span class="box"></span>DOWNLOAD</li><li class="step">→ Flagship Content</li><li class="step">→ Premium Content</li><li class="step">→ E-books</li><li class="step">→ Templates</li>
  </ul></div>
  <svg class="diagram" viewBox="0 0 566 414" aria-hidden="true">
    <circle cx="207" cy="74" r="8" fill="#fff"/><circle cx="205.5" cy="72.5" r="3" fill="none" stroke="#1f63b4" stroke-width="1.2"/><line x1="207.5" y1="74.5" x2="210.5" y2="77.5" stroke="#1f63b4" stroke-width="1.4"/>
    <text x="218" y="76" font-size="11">SEO</text><text x="214" y="84" font-size="5">Organic Searches</text>
    <circle cx="298" cy="74" r="8" fill="#fff"/><circle cx="298" cy="74" r="4.5" fill="#2f93e0"/>
    <text x="309" y="76" font-size="11">SEM</text><text x="309" y="84" font-size="5">Seekly Ads</text>
    <g stroke="#fff" stroke-width="1" fill="none"><path d="M245 89V103M242 100l3 3 3-3"/><path d="M326 89V103M323 100l3 3 3-3"/><path d="M342 209H384M380 206l4 3-4 3"/></g>
    <circle cx="282" cy="164" r="52" fill="none" stroke="#fff" stroke-width="2.2"/>
    <circle cx="282" cy="303" r="84" fill="none" stroke="#fff" stroke-width="2.2"/>
    <circle cx="282" cy="168" r="33" fill="var(--website-blue)" stroke="var(--website-light)" stroke-width="2"/>
    <text x="282" y="164" font-size="10.5" text-anchor="middle">Website</text>
    <rect x="270" y="170" width="24" height="13" fill="#fff"/><rect x="270" y="170" width="24" height="3" fill="#9cc9ee"/>
    <circle cx="282" cy="305" r="53" fill="var(--magenta)" stroke="var(--magenta-light)" stroke-width="2"/>
    <text x="282" y="298" font-size="11" text-anchor="middle">Social Media</text>
    <text x="282" y="311" font-size="11" text-anchor="middle">Content &amp;</text>
    <text x="282" y="324" font-size="11" text-anchor="middle">Marketing</text>
    <g stroke="#dce8f5" stroke-width="1.5" fill="#fff">
      <circle cx="282" cy="111" r="13"/><circle cx="231" cy="169" r="11"/><circle cx="336" cy="164" r="11"/><circle cx="282" cy="218" r="11"/>
      <circle cx="330" cy="236" r="11"/><circle cx="358" cy="268" r="11"/><circle cx="364" cy="304" r="11"/><circle cx="356" cy="344" r="11"/>
      <circle cx="329" cy="374" r="11"/><circle cx="282" cy="387" r="11"/><circle cx="238" cy="374" r="11"/><circle cx="210" cy="344" r="11"/>
      <circle cx="202" cy="304" r="11"/><circle cx="209" cy="268" r="11"/><circle cx="235" cy="232" r="11"/>
    </g>
    <rect x="274" y="104" width="16" height="11" fill="#2f93e0"/><rect x="279" y="115" width="6" height="3" fill="#777"/>
    <rect x="227" y="162" width="8" height="14" rx="1.5" fill="#2f93e0"/>
    <rect x="331" y="158" width="10" height="12" fill="#f0c36a"/>
    <circle cx="282" cy="218" r="7.5" fill="#f39a1e"/>
    <circle cx="330" cy="236" r="7.5" fill="#2d4f8f"/><circle cx="358" cy="268" r="7.5" fill="#1e7cc2"/>
    <circle cx="364" cy="304" r="7.5" fill="#d4483a"/><circle cx="356" cy="344" r="7.5" fill="#45b3e8"/>
    <circle cx="329" cy="374" r="7.5" fill="#6c3fa0"/><circle cx="282" cy="387" r="7.5" fill="#2f93e0"/>
    <circle cx="238" cy="374" r="7.5" fill="#4a4541"/><circle cx="210" cy="344" r="7.5" fill="#c8232c"/>
    <circle cx="202" cy="304" r="7.5" fill="#2fb07a"/><circle cx="235" cy="232" r="7.5" fill="#d8342e"/>
    <rect x="203" y="264" width="12" height="8" fill="#c9ccd1"/><path d="M203 264l6 4.5 6-4.5" fill="none" stroke="#888" stroke-width="0.8"/>
    <g font-size="5.5">
      <text x="216" y="165" text-anchor="end">Mobile &amp; Tablet</text><text x="216" y="171" text-anchor="end">Friendly Site</text>
      <text x="352" y="166">Landing Pages</text>
      <text x="282" y="237" text-anchor="middle">Blog</text>
      <text x="344" y="235">Mingle</text><text x="372" y="270">ProLink</text><text x="378" y="306">Seekly Plus</text>
      <text x="370" y="346">Chirper</text><text x="343" y="374">Podcasts &amp;</text><text x="343" y="380">Webinars</text>
      <text x="282" y="405" text-anchor="middle">Apps</text>
      <text x="223" y="376" text-anchor="end">Photon</text><text x="196" y="346" text-anchor="end">Pinspace</text>
      <text x="188" y="302" text-anchor="end">Loopy</text>
      <text x="195" y="264" text-anchor="end">Email</text><text x="195" y="270" text-anchor="end">Marketing</text>
      <text x="221" y="234" text-anchor="end">Vidora</text>
    </g>
  </svg>
  <p class="footnote">* Start with the website, then point every search, link and social channel back to it. Tick each back link you can win, choose one outcome per visitor and review the results monthly so you can see which channels bring real enquiries.</p>
  <div class="corner"></div>
  <div class="brand"><span class="brand-dot"></span><span>CLOUDLINE<br>DIGITAL</span></div>
</section>

<!-- Planning table sheet, second row -->
<section class="sheet at-bottom at-right">
  <header class="sheet-tab wide"><span class="tab-mark"></span>Web Strategy Planning</header>
  <div class="client-fields"><div><span>COMPANY:</span><i></i></div><div><span>PRODUCT/SERVICE:</span><i></i></div></div>
  <div class="plan-table">
    <div class="plan-row shaded row-who"><div class="row-label">WHO</div><div><div class="q-main">Buyer Persona</div><div class="q-main">Description</div><div class="q-note">Who is this person?</div></div><div>1:</div><div>2:</div></div>
    <div class="plan-row row-what"><div class="row-label">WHAT</div><div><div class="q-split"><div class="q-main">Problems you solve for this buyer?</div><div class="q-note">Why are they buying from you?</div></div><div class="q-main">Actions you'd like them to take:</div><div class="q-note">Purchase</div><div class="q-note">Enquire</div><div class="q-note">Connect</div><div class="q-note">Download</div></div><div></div><div></div></div>
    <div class="plan-row shaded row-why"><div class="row-label">WHY</div><div><div class="q-main">How are you remarkable?</div><div class="q-main" style="margin-top:6px">Proof</div><div class="q-note">Guarantees, testimonials, press etc</div></div><div></div><div></div></div>
    <div class="plan-row row-where"><div class="row-label">WHERE</div><div><div class="q-main">Where are they?</div><div class="q-note">Seekly, blogs, Mingle, Chirper etc</div><div class="q-note">Who do they trust?</div></div><div></div><div></div></div>
    <div class="plan-row shaded row-how"><div class="row-label">HOW</div><div><div class="q-main">Content is King (Strategy)</div><div class="q-note">What will you publish?</div><div class="q-gap"></div><div class="q-note">Keywords buyers type into Seekly.</div><div class="q-main" style="margin-top:3px">Marketing is Queen (Tactics)</div><div class="q-note">Blog, Chirper, Vidora, email newsletter, e-books, Mingle podcasts etc</div></div><div></div><div></div></div>
    <div class="row-when">
      <div class="row-label">WHEN</div>
      <div class="when-lines"><div><span>Things to do this week:</span></div><div><span>... this month:</span></div><div><span>... this quarter:</span></div><div><span>... this year:</span></div></div>
      <div class="score-tag">SCORECARD</div>
      <div class="score-lines"><div>No. of Purchases:</div><div>No. of Enquiries:</div><div>No. of Connections:</div><div>No. of Downloads:</div></div>
      <div class="score-head">GOAL</div>
      <div class="score-head">RESULT</div>
    </div>
  </div>
  <p class="footnote wide">* Fill in one column per buyer persona. Describe who they are, what problem you solve, where they spend time online and which actions you want them to take, then set weekly goals.</p>
  <p class="footnote wide">* Use the scorecard to record each goal beside its result at the end of every month, and move effort towards the channels that bring the most purchases, enquiries, connections and downloads.</p>
  <div class="corner"></div>
  <div class="brand"><span class="brand-dot"></span><span>CLOUDLINE<br>DIGITAL</span></div>
</section>

</body>
</html>
```